Bright Harbor Painting and Remodeling needs a business card

Business card should have company logo. I will upload two different logos and let me see which one is a better design for the business card.

Name of company: Bright Harbor Painting and Remodeling
Address: 4826 NW 61st st Suite 214
Miami, FL 33172

local phone: (305) 555-0143
toll free (855) 555-0176
fax (866) 555-0128

email: darla@brightharborcoats.example

not sure if i should include social media links or names on the business card.

company does interior and exterior painting, pressure washing, wall paper removal, drywall and stucco repair, staining,

We give free estimates.

I want a two sided business card.

Not sure if all this information is necessary for the business card. Designer can pick out whatever information they deem is important for a consumer to see on the business card.

Anticipating on the business card to be printed on nice quality.

I will upload an image of one of the logos on a type of business card surface. That idea can be used as well. Be creative. Business card should be professional but very nice and eye catching.

remove drywall and stucco repair and replace with tile installation

Industry/Entity Type

Business

Contact Information for Business Card

Miami, FL 33172

toll free (855) 555-0176
fax (866) 555-0128

company does interior and exterior painting, pressure washing, wall paper removal, drywall and stucco repair, staining, tile removal, *specializing in vinyl floor removal

free estimates.

Requirements
Must have
• Profesional font

```html
<!DOCTYPE html>
<html lang="en">
<head>
<meta charset="utf-8">
<title>Bright Harbor Painting and Remodeling – Business Card</title>
<link rel="stylesheet" href="https://fonts.googleapis.com/css2?family=Roboto+Slab:wght@400;600&family=Vollkorn:wght@400;600&display=swap">
<style>
  :root{
    --stage:#e9e9ea;
    --card-black:#050505;
    --card-white:#ffffff;
    --brand-blue:#0a6fb8;
    --brand-orange:#f6a236;
    --services-yellow:#f2e24a;
    --text-light:#ffffff;
    --text-dark:#3a3a3a;
    --logo-yellow:#f7d66b;
    --social-red:#c9362b;
  }
  *{box-sizing:border-box;margin:0;padding:0}
  html,body{width:1200px;height:880px;overflow:hidden;background:var(--stage)}
  .canvas{position:relative;width:1200px;height:880px}
  .card{position:absolute;width:700px;height:400px;border-radius:22px;overflow:hidden;box-shadow:0 8px 24px rgba(0,0,0,.18)}

  /* back side */
  .card--back{left:60px;top:30px;background:var(--card-black);color:var(--text-light);font-family:"Vollkorn",serif}
  .services{position:absolute;left:48px;top:62px}
  .services__title{font-weight:600;font-size:26px;color:var(--services-yellow);letter-spacing:.5px;margin-bottom:8px}
  .services__list{list-style:none}
  .services__item{display:flex;align-items:center;gap:12px;font-size:19px;line-height:28px}
  .services__item::before{content:"";width:10px;height:10px;border-radius:50%;background:var(--services-yellow);flex:none}
  .services__item--feature{color:var(--services-yellow)}
  .estimates{position:absolute;left:48px;top:292px;font-family:"Roboto Slab",serif;font-size:24px;color:var(--services-yellow);letter-spacing:1px}
  .social{position:absolute;left:48px;top:340px;display:flex;gap:8px}
  .social__box{width:26px;height:26px;border-radius:3px;background:var(--brand-blue)}
  .social__box--red{background:var(--social-red)}
  .website{position:absolute;left:196px;top:339px;font-size:19px;line-height:28px}
  .website__domain{color:var(--services-yellow)}
  .back-mark{position:absolute;right:50px;top:95px;width:220px;display:flex;flex-direction:column;align-items:center;gap:16px;text-align:center}
  .back-mark__circle{width:130px;height:130px;border-radius:50%;background:var(--logo-yellow)}
  .back-mark__name{font-family:"Roboto Slab",serif;font-weight:600;font-size:18px;line-height:24px;color:var(--text-light)}

  /* front side */
  .card--front{left:440px;top:450px;background:var(--card-white);font-family:"Roboto Slab",serif}
  .front-art{position:absolute;inset:0}
  .front-mark{position:absolute;left:40px;top:120px;display:flex;align-items:center;gap:14px;width:300px}
  .front-mark__circle{width:64px;height:64px;border-radius:50%;background:var(--logo-yellow);flex:none}
  .front-mark__name{font-weight:600;font-size:18px;line-height:23px;color:var(--text-dark)}
  .person{position:absolute;right:36px;top:34px;text-align:right}
  .person__name{font-weight:600;font-size:26px;color:var(--brand-blue)}
  .person__title{font-size:17px;color:var(--brand-orange);margin-top:-2px}
  .contact{position:absolute;right:30px;top:212px;text-align:right;color:var(--text-light);font-size:14px;line-height:22px;font-style:normal}
  .contact__label{color:var(--brand-orange);font-weight:600}
</style>
</head>
<body>
<main class="canvas">

  <section class="card card--back" aria-label="Card back: services">
    <div class="services">
      <h2 class="services__title">OUR SERVICES</h2>
      <ul class="services__list">
        <li class="services__item">Interior and Exterior Painting</li>
        <li class="services__item">Pressure Washing</li>
        <li class="services__item">Staining</li>
        <li class="services__item">Wall Paper Removal</li>
        <li class="services__item">Tile Installation and Removal</li>
        <li class="services__item services__item--feature">Specializing in Vinyl Floor Removal</li>
      </ul>
    </div>
    <p class="estimates">Free Estimates</p>
    <div class="social" aria-hidden="true">
      <span class="social__box"></span>
      <span class="social__box"></span>
      <span class="social__box"></span>
      <span class="social__box social__box--red"></span>
    </div>
    <p class="website">www.<span class="website__domain">brightharborcoats</span>.example</p>
    <div class="back-mark">
      <span class="back-mark__circle" aria-hidden="true"></span>
      <span class="back-mark__name">Bright Harbor Painting and Remodeling</span>
    </div>
  </section>

  <section class="card card--front" aria-label="Card front: contact">
    <svg class="front-art" viewBox="0 0 700 400" aria-hidden="true">
      <path d="M700,100 C560,105 470,150 430,220 C390,290 340,370 250,400 L700,400 Z" fill="#0a6fb8"/>
      <path d="M232,396 C320,366 362,286 402,212 C442,140 545,88 700,78" fill="none" stroke="#0a6fb8" stroke-width="6"/>
      <path d="M0,350 C150,350 230,330 280,272 C305,240 318,205 330,178" fill="none" stroke="#f6a236" stroke-width="14"/>
      <path d="M0,376 C110,382 180,380 230,372 L246,400 L0,400 Z" fill="#0a6fb8"/>
    </svg>
    <div class="front-mark">
      <span class="front-mark__circle" aria-hidden="true"></span>
      <span class="front-mark__name">Bright Harbor Painting and Remodeling</span>
    </div>
    <div class="person">
      <p class="person__name">Marcus Hale</p>
      <p class="person__title">Director</p>
    </div>
    <address class="contact">
      <p><span class="contact__label">Phone:</span> (305) 555-0143</p>
      <p><span class="contact__label">Toll Free:</span> (855) 555-0176</p>
      <p><span class="contact__label">Fax:</span> (866) 555-0128</p>
      <p><span class="contact__label">Email:</span> darla@brightharborcoats.example</p>
      <p>4826 NW 61st st Suite 214</p>
      <p>Miami, FL 33172</p>
    </address>
  </section>

</main>
</body>
</html>
```